【 概要 】 不登校の子供を持つ親御さんをターゲットにした、心理系Clipnestチャンネルを運営しております。 ・ターゲット層:子どもの不登校で不安を抱える30~50代女性 ・雰囲気:心理系、子育て系 クリック率が上がるようなサムネイル・タイトルを製作してくださる方を募集しています。 文言・デザインは制作者の方に一任する予定です。 【 今回の依頼内容 】 こちらの2つの動画のサムネイル・タイトルを、それぞれ製作してください ・動画A 動画:https://clpn.st/k3TfQw9LmZr 台本:https://pages.fernleaf.io/sheet/d/7qX4Lm-pTzR2VbNcWkHyEsUaGdJ0oPfM9tK3n582QrVx/edit?usp=sharing ・動画B 動画:https://clpn.st/r8HzDq4XbNe 台本:https://pages.fernleaf.io/sheet/d/9vKTe2_WbLJ6YxRtPq5Hn4DgUfAmCsVo8Zre3jw6PLu/edit?usp=sharing 【サムネイルについて】 ・サイズ: 横1920 × 縦1080px ・作成数: 1動画につき1種類 ・ファイル形式:PNG ・女性の顔(胸から上)を入れてください。今回はテストなので、無料素材サイトから取得をお願いします。 ・それ以外のデザインの部分については、センスにお任せします! 【タイトルについて】 ・検索流入を増やしたいので、検索に最適化したタイトル(検索ワードをそのまま入れたタイトル)にしていただけると幸いです ・原則1動画1案のご提出で構いませんが、複数案ある方はご提示ください 【 報酬 】 継続契約後の基本報酬は1動画5,000円と考えております また公開48時間後のクリック率に応じて以下のチップを追加でお支払いします 8%~ +3000円 5~8% +1500円 ~5% 0円 このあたりは、ご契約時にご相談して決めていければと思っております。 またクオリティが高い方や、コミュニケーションが丁寧な方などは 契約後も定期的に単価アップをしていきたいと考えています。 疑問点・質問等ございましたらお気軽にご連絡ください。 ご応募お待ちしております! |

```html
<!DOCTYPE html>
<html lang="ja">
<head>
<meta charset="utf-8">
<title>不登校が早く解決するご家庭に共通する特徴３選</title>
<link href="https://fonts.googleapis.com/css2?family=Noto+Sans+JP:wght@900&display=swap" rel="stylesheet">
<style>
  :root {
    --band-pink: #f9d3e3;
    --title-pink: #e0306f;
    --headline-red: #ea1a5c;
    --accent-yellow: #fff100;
    --outline: #ffffff;
    --bg-cream: #fff8f2;
    --bg-rose: #fbd9e6;
    --bg-gold: #fde9b4;
  }
  html, body {
    margin: 0;
    padding: 0;
    width: 1200px;
    height: 676px;
    overflow: hidden;
  }
  .thumbnail {
    position: relative;
    width: 1200px;
    height: 676px;
    overflow: hidden;
    font-family: "Noto Sans JP", sans-serif;
    font-weight: 900;
    background:
      radial-gradient(circle at 62% 42%, #ffffff 0%, rgba(255,255,255,0) 30%),
      radial-gradient(circle at 88% 30%, var(--bg-gold) 0%, rgba(253,233,180,0) 25%),
      radial-gradient(circle at 20% 60%, var(--bg-rose) 0%, rgba(251,217,230,0) 35%),
      radial-gradient(circle at 95% 85%, var(--bg-rose) 0%, rgba(251,217,230,0) 30%),
      var(--bg-cream);
  }
  .top-band {
    position: absolute;
    left: 0;
    top: 0;
    width: 1200px;
    height: 100px;
    background: var(--band-pink);
    display: flex;
    align-items: center;
    justify-content: center;
  }
  .tagline {
    margin: 0;
    font-size: 78px;
    line-height: 1;
    letter-spacing: 1px;
    color: var(--title-pink);
    -webkit-text-stroke: 8px var(--outline);
    paint-order: stroke fill;
    white-space: nowrap;
  }
  .presenter-photo {
    position: absolute;
    left: 40px;
    top: 100px;
    width: 430px;
    height: 576px;
    background: linear-gradient(180deg, #e9e4e1 0%, #d9d6d4 55%, #cfcdcc 100%);
    border-radius: 200px 200px 0 0;
  }
  .headline {
    position: absolute;
    left: 470px;
    top: 150px;
    width: 730px;
    margin: 0;
    text-align: center;
    color: var(--headline-red);
    -webkit-text-stroke: 12px var(--outline);
    paint-order: stroke fill;
    line-height: 1.22;
  }
  .headline .line-1 { display: block; font-size: 124px; }
  .headline .line-2 { display: block; font-size: 118px; }
  .footer-row {
    position: absolute;
    left: 20px;
    top: 544px;
    width: 1170px;
    height: 106px;
    display: flex;
    align-items: center;
    gap: 20px;
  }
  .footer-lead {
    font-size: 76px;
    line-height: 1;
    color: var(--headline-red);
    -webkit-text-stroke: 10px var(--outline);
    paint-order: stroke fill;
    white-space: nowrap;
  }
  .footer-badge {
    flex: 1;
    height: 106px;
    background: var(--accent-yellow);
    display: flex;
    align-items: center;
    justify-content: center;
    font-size: 100px;
    line-height: 1;
    color: var(--headline-red);
    white-space: nowrap;
  }
</style>
</head>
<body>
  <main class="thumbnail">
    <header class="top-band">
      <p class="tagline">自分が変われば周りも変わる？</p>
    </header>
    <div class="presenter-photo" role="img" aria-label="笑顔の女性（胸から上）の写真"></div>
    <h1 class="headline">
      <span class="line-1">不登校が</span>
      <span class="line-2">早く解決する</span>
    </h1>
    <div class="footer-row">
      <span class="footer-lead">ご家庭に共通する</span>
      <span class="footer-badge">特徴３選</span>
    </div>
  </main>
</body>
</html>
```